Book Cover (Front and Rear) for E book called Quiet Mazes

Create book cover front and rear book cover for e book called quiet mazes. Quiet Mazes is a book of 99 puzzles made up of Sudoku, word scrambles, word searches, cross words, mine finder.

Looking for a fairly simple cover similar to the attached 2 designs. Must mention title of book (quiet mazes) as well as making it clear that it is a book of puzzles and my name as the author (Hollis Varga). Rear cover basically same colour as front however just plain.

```html
<!DOCTYPE html>
<html lang="en">
<head>
<meta charset="utf-8">
<title>Quiet Mazes – Book Cover Spread</title>
<link href="https://fonts.googleapis.com/css2?family=Bebas+Neue&family=Oswald:wght@200;500&family=Roboto+Condensed:wght@500&family=Arimo:wght@400&display=swap" rel="stylesheet">
<style>
  :root {
    --page-bg: #f4f4f4;
    --cream: #fdf0dc;
    --cream-light: #fef6ea;
    --orange: #f9ae41;
    --red: #ec1c24;
    --body-ink: #2a2422;
    --ink: #111111;
    --rule: #8a7bb0;
  }
  * { margin: 0; padding: 0; box-sizing: border-box; }
  html, body {
    width: 1200px; height: 1200px; overflow: hidden;
    background: var(--page-bg);
  }
  .spread {
    position: absolute; left: 0; top: 168px;
    width: 1200px; height: 864px;
    background: radial-gradient(ellipse at 78% 62%, var(--cream-light) 0%, var(--cream) 60%);
  }

  /* Back cover */
  .back-cover { position: absolute; left: 0; top: 0; width: 580px; height: 864px; }
  .back-title {
    position: absolute; left: 0; width: 580px; top: 52px;
    text-align: center; font-family: "Bebas Neue", sans-serif;
    font-size: 92px; line-height: 76px;
  }
  .back-title .word-a { color: var(--orange); display: block; }
  .back-title .word-b { color: var(--orange); display: block; }
  .back-subtitle {
    position: absolute; left: 180px; width: 220px; top: 215px;
    text-align: center; font-family: "Oswald", sans-serif; font-weight: 500;
    font-size: 11.5px; line-height: 15px; color: var(--red); letter-spacing: -0.2px;
  }
  .back-rule {
    position: absolute; left: 104px; top: 277px; width: 367px; height: 1px;
    background: linear-gradient(90deg, transparent, var(--rule) 20%, var(--rule) 80%, transparent);
  }
  .back-blurb {
    position: absolute; left: 56px; width: 460px; top: 300px;
    text-align: center; font-family: "Arimo", sans-serif;
    font-size: 12.8px; line-height: 20px; color: var(--body-ink);
  }
  .back-blurb p + p { margin-top: 20px; }

  /* Spine */
  .spine-title, .spine-subtitle, .spine-author {
    position: absolute; writing-mode: vertical-rl;
  }
  .spine-title {
    left: 583px; top: 57px;
    font-family: "Bebas Neue", sans-serif; font-size: 27px; color: var(--red);
    line-height: 27px; letter-spacing: 0.3px;
  }
  .spine-divider {
    position: absolute; left: 587px; top: 198px; width: 16px; height: 1px; background: var(--ink);
  }
  .spine-subtitle {
    left: 586px; top: 214px; height: 250px;
    font-family: "Roboto Condensed", sans-serif; font-weight: 500;
    font-size: 9px; line-height: 11px; color: var(--ink); letter-spacing: 1px;
  }
  .spine-author {
    left: 584px; top: 733px;
    font-family: "Oswald", sans-serif; font-weight: 200; font-size: 16px;
    line-height: 18px; color: var(--ink);
  }

  /* Front cover */
  .front-cover { position: absolute; left: 616px; top: 0; width: 584px; height: 864px; }
  .front-title {
    position: absolute; left: 0; width: 584px; top: 50px;
    text-align: center; font-family: "Bebas Neue", sans-serif;
    font-size: 150px; line-height: 118px;
  }
  .front-title .word-a { color: var(--orange); display: block; }
  .front-title .word-b { color: var(--red); display: block; }
  .front-subtitle {
    position: absolute; left: 60px; width: 464px; top: 300px;
    text-align: center; font-family: "Oswald", sans-serif; font-weight: 500;
    font-size: 17px; line-height: 24px; color: var(--orange); letter-spacing: -0.3px;
  }
  .puzzle-art {
    position: absolute; left: 108px; top: 396px; width: 314px; height: 340px;
    border-radius: 40px;
    background:
      radial-gradient(circle at 28% 26%, #a9e6cf 0%, transparent 38%),
      radial-gradient(circle at 72% 24%, #f6b887 0%, transparent 40%),
      radial-gradient(circle at 26% 72%, #f88078 0%, transparent 38%),
      radial-gradient(circle at 70% 72%, #a9d3e4 0%, transparent 40%),
      var(--cream);
  }
  .front-author {
    position: absolute; left: 0; width: 584px; top: 770px;
    text-align: center; font-family: "Bebas Neue", sans-serif;
    font-size: 60px; line-height: 60px; color: var(--red); letter-spacing: 12px;
  }
</style>
</head>
<body>
  <div class="spread">
    <section class="back-cover">
      <h2 class="back-title"><span class="word-a">QUIET</span><span class="word-b">MAZES</span></h2>
      <p class="back-subtitle">99 PUZZLES MADE UP OF SUDOKU, WORD SCRAMBLES, WORD SEARCHES, CROSS WORDS, MINE FINDER.</p>
      <div class="back-rule"></div>
      <div class="back-blurb">
        <p>Lorem ipsum dolor sit amet, consectetuer adipiscing elit, sed diam nonummy nibh euismod tincidunt ut laoreet dolore magna aliquam erat volutpat. Ut wisi enim ad minim veniam, quis nostrud exerci tation ullamcorper suscipit lobortis nisl ut aliquip ex ea commodo consequat. Duis autem vel eum iriure dolor in hendrerit in vulputate velit esse molestie consequat, vel illum dolore eu feugiat nulla facilisis at vero eros et accumsan et iusto odio dignissim qui blandit praesent luptatum zzril delenit augue duis dolore te feugait nulla facilisi.</p>
        <p>Lorem ipsum dolor sit amet, cons ectetuer adipiscing elit, sed diam nonummy nibh euismod tincidunt ut laoreet dolore magna aliquam erat volutpat. Ut wisi enim ad minim veniam, quis nostrud exerci tation ullamcorper suscipit lobortis nisl ut aliquip ex ea commodo consequat.</p>
        <p>Ut wisi enim ad minim veniam, quis nostrud exerci tation ullamcorper suscipit lobortis nisl ut aliquip ex ea commodo consequat.</p>
      </div>
    </section>

    <div class="spine-title">QUIET MAZES</div>
    <div class="spine-divider"></div>
    <div class="spine-subtitle">99 PUZZLES MADE UP OF SUDOKU, WORD SCRAMBLES, WORD SEARCHES, CROSS WORDS, MINE FINDER.</div>
    <div class="spine-author">HOLLIS VARGA</div>

    <section class="front-cover">
      <h1 class="front-title"><span class="word-a">QUIET</span><span class="word-b">MAZES</span></h1>
      <p class="front-subtitle">99 PUZZLES MADE UP OF SUDOKU, WORD SCRAMBLES, WORD SEARCHES, CROSS WORDS, MINE FINDER.</p>
      <div class="puzzle-art" role="img" aria-label="Four soft 3D jigsaw pieces in mint, peach, coral and pale blue floating apart"></div>
      <p class="front-author">HOLLIS VARGA</p>
    </section>
  </div>
</body>
</html>
```